WordPress Website Design for Multi-Brand Aviation Group (Unified Branding System)

Project Overview:
We are seeking a professional, modern WordPress website design for an aviation-focused umbrella company that owns and operates multiple subsidiary businesses. The goal is to create a cohesive visual system that clearly communicates that each company operates under the same parent organization, while still allowing each brand to maintain a slightly distinct identity.
This is not just a single website design—we are looking for a scalable design framework that can be applied across multiple aviation-related businesses.
Objectives:
- Establish a consistent, recognizable brand identity across all company websites
Clearly communicate the relationship between the parent company and its subsidiaries
-bCreate a clean, high-end corporate aviation aesthetic
- Ensure all designs are SEO-friendly and optimized for performance
- Allow flexibility for future expansion (additional subsidiaries)
- Target Audience:
- Corporate aviation clients
- Charter customers
- Students wishing to receive flight training
- Aircraft owners and operators
- Turbine aircraft training to meet insurance requirements
- Business professionals and high-net-worth individuals
- Aviation industry partners
Design Direction & Style:
We are looking for a premium, professional aviation feel—think clean, modern, and high-trust. The design should reflect the standards of corporate aviation: precision, safety, and sophistication.
Key style notes:
Minimalist but impactful layout
High-quality aviation photography (jets, interiors, operations, global travel)
Subtle motion/interaction (hover effects, transitions)
Clear typography hierarchy for readability and professionalism
Branding Requirements:
Incorporate the primary colors of the parent company logo across all designs
Website Structure (Core Pages):
Design a system that includes:
Home Page with the following links:
- About / Company Overview
- Aircraft Management
- Aircraft Acquisition
- Charter
- Pilot Services
- Trip Support
- Contact Page
Site should further include:
- Mobile-first responsive design
- Fast-loading, performance-optimized layouts
SEO & Technical Considerations:
- Design should support high-level SEO implementation:
- Clean layout structure that translates well to semantic HTML
- Proper heading hierarchy (H1, H2, H3)
- Space for keyword-rich content without clutter
- Optimized image placement (with alt text capability)
- Fast load times (lightweight design approach)
- Compatibility with WordPress SEO plugins (e.g., Yoast or Rank Math)
WordPress Requirements:
- Design should be easily built using WordPress (preferred builders: Elementor, Gutenberg, or similar)
- Reusable templates for scalability across multiple sites
- Easy for non-developers to update text and images
- Modular components (blocks/sections that can be reused across pages and sites)
- Navigation & UX:
- Simple, intuitive navigation
- Sticky header preferred
Style guide including:
- Colors
- Fonts
- Button styles
- Layout system
- Designs similar to high-end corporate aviation, private jet charter, or luxury service brands are preferred—clean, sharp, and premium without being overly flashy.
What We Want to Avoid:
- Overly busy layouts
- Generic templates with no brand identity
- Outdated or “stock” looking aviation designs
- Poor mobile responsiveness
Additional Notes:
We are building a long-term brand system, not just a one-off website. There is potential for ongoing work as we expand additional subsidiary sites.
We value designers who understand branding consistency across multiple business units and can create a scalable, professional system.
Include the attached main company logo "Tarnwell Aviation Group" and the "Member FLTC" logo on the main page.
1 page

```html
<!DOCTYPE html>
<html lang="en">
<head>
<meta charset="utf-8">
<title>Tarnwell Aviation Group — Precision Aviation. Unified Excellence.</title>
<link href="https://fonts.googleapis.com/css2?family=Poppins:wght@400;500;600&display=swap" rel="stylesheet">
<style>
:root{
  --navy:#0b2a57;
  --navy-deep:#061c3f;
  --blue:#0a52a8;
  --ink:#0f1e33;
  --muted:#3d4a5c;
  --white:#ffffff;
  --card-shadow:0 6px 18px rgba(10,35,80,.12);
}
*{box-sizing:border-box;margin:0;padding:0}
html,body{width:1200px;height:3750px;overflow:hidden}
body{font-family:"Poppins",sans-serif;color:var(--ink);background:var(--white);position:relative}
a{color:inherit;text-decoration:none}
.eyebrow{font-size:15px;font-weight:500;letter-spacing:.4px;color:var(--blue)}
.btn{display:inline-flex;align-items:center;justify-content:center;gap:12px;height:44px;padding:0 16px;font-size:12px;font-weight:500;letter-spacing:.4px;border-radius:3px;white-space:nowrap}
.btn-primary{background:var(--blue);color:var(--white)}
.btn-outline{border:1px solid rgba(255,255,255,.7);color:var(--white)}
.arrow-link{font-size:10px;font-weight:500;color:var(--blue);display:inline-flex;gap:8px;align-items:center;letter-spacing:.3px;white-space:nowrap}

/* header */
.site-header{position:absolute;top:0;left:0;width:1200px;height:98px;background:var(--white);border-bottom:1px solid #e3e8ef}
.brand{position:absolute;left:40px;top:30px;display:flex;align-items:center;gap:10px}
.brand-mark{width:14px;height:14px;background:var(--blue)}
.brand-name{font-size:17px;font-weight:600;color:var(--navy);letter-spacing:.3px;line-height:1.1}
.main-nav{position:absolute;left:247px;top:45px;display:flex;gap:28px;font-size:11.5px;letter-spacing:.3px;color:var(--ink);white-space:nowrap}
.nav-cta{position:absolute;left:1027px;top:33px;width:136px;height:40px;border-radius:4px;background:var(--blue);color:var(--white);font-size:11.5px;display:flex;align-items:center;justify-content:center;letter-spacing:.3px}

/* hero */
.hero{position:absolute;top:98px;left:0;width:1200px;height:580px;color:var(--white);overflow:hidden}
.hero-photo{position:absolute;inset:0;background:linear-gradient(90deg,#0b2453 0%,#123a73 45%,#4b5a78 75%,#a27a5a 100%)}
.hero-shade{position:absolute;inset:0;background:linear-gradient(180deg,rgba(6,28,63,0) 40%,rgba(6,20,45,.75) 100%)}
.hero .eyebrow{color:var(--white);font-size:11px;position:absolute;left:208px;top:63px}
.hero h1{position:absolute;left:208px;top:90px;font-size:46px;line-height:55px;font-weight:600}
.hero-lede{position:absolute;left:211px;top:225px;width:400px;font-size:11.5px;line-height:19px}
.hero-actions{position:absolute;left:209px;top:298px;display:flex;gap:12px}
.trust{position:absolute;left:211px;top:364px;font-size:11.5px;display:flex;gap:6px;align-items:center}
.trust span{color:#5f8fd6}
.feature-bar{display:flex;justify-content:space-between;padding:0 16px;align-items:center;border-radius:6px}
.hero .feature-bar{position:absolute;left:208px;top:427px;width:782px;height:110px;border:1px solid rgba(120,160,220,.45);background:rgba(8,30,70,.45)}
.feature{display:flex;gap:12px;align-items:flex-start}
.feature h3{font-size:11px;font-weight:500;letter-spacing:.3px;margin-bottom:6px;white-space:nowrap}
.feature p{font-size:9.5px;line-height:15px;width:136px}
.feature svg{flex:none;margin-top:2px}

/* about */
.about{position:absolute;top:678px;left:0;width:1200px;height:622px;background:linear-gradient(90deg,#eef1f6 0%,#ffffff 30%)}
.center{text-align:center;width:100%}
.about .eyebrow{position:absolute;top:56px}
.about h2,.services h2{position:absolute;font-size:31px;font-weight:600}
.about h2{top:86px}
.about .lead{position:absolute;top:144px;left:280px;width:640px;font-size:14.5px;line-height:23px;text-align:center}
.pill-row{position:absolute;top:213px;left:244px;width:714px;height:52px;display:flex;align-items:center}
.pill-row::before,.pill-row::after{content:"";flex:1;height:1px;background:#c5d4e8}
.pill{width:255px;height:52px;border-radius:26px;background:var(--blue);color:var(--white);font-size:15.5px;display:flex;align-items:center;justify-content:center;letter-spacing:.3px}
.company-card{position:absolute;top:305px;width:237px;height:237px;background:var(--white);border-radius:6px;box-shadow:var(--card-shadow);padding:24px 22px}
.company-head{display:flex;gap:12px;align-items:center;margin-bottom:28px}
.icon-ring{width:52px;height:52px;border-radius:50%;border:2px solid var(--blue);display:flex;align-items:center;justify-content:center;flex:none}
.company-name{font-size:16px;font-weight:600;color:var(--blue);letter-spacing:.5px;line-height:1.1}
.company-sub{font-size:11px;font-weight:500;color:var(--ink);margin-top:4px}
.company-card p{font-size:10px;line-height:19px;color:var(--muted);margin-bottom:22px;padding-left:4px}
.company-card .arrow-link{padding-left:4px}
.carousel-btn{position:absolute;width:26px;height:26px;border-radius:50%;border:1px solid #5a6472;display:flex;align-items:center;justify-content:center}

/* services */
.services{position:absolute;top:1300px;left:0;width:1200px;height:700px}
.services-band{position:absolute;top:0;left:0;width:1200px;height:411px;background:linear-gradient(180deg,#0a2450,#0c3066)}
.services .eyebrow{position:absolute;top:58px;color:var(--white)}
.services h2{top:90px;color:var(--white)}
.services .lead{position:absolute;top:144px;left:280px;width:640px;font-size:14.5px;line-height:23px;text-align:center;color:var(--white)}
.service-card{position:absolute;top:227px;width:211px;height:431px;background:var(--white);border-radius:4px;box-shadow:var(--card-shadow)}
.service-photo{height:182px;border-radius:4px 4px 0 0}
.service-icon{position:absolute;left:77px;top:153px;width:58px;height:58px;border-radius:50%;background:var(--white);box-shadow:0 2px 8px rgba(0,0,0,.15);display:flex;align-items:center;justify-content:center}
.service-body{padding:38px 20px 0 30px}
.service-body h3{font-size:15.5px;font-weight:500;line-height:22px;height:48px;display:flex;align-items:center;margin-bottom:18px}
.checklist{list-style:none;font-size:10px;line-height:19px;margin-bottom:16px;white-space:nowrap}
.checklist li{display:flex;gap:7px;align-items:center}
.checklist li::before{content:"";flex:none;width:8px;height:4px;border-left:1.5px solid var(--blue);border-bottom:1.5px solid var(--blue);transform:rotate(-45deg) translateY(-2px)}

/* why */
.why{position:absolute;top:2030px;left:0;width:1200px;height:480px;overflow:hidden}
.why .eyebrow{position:absolute;left:208px;top:36px}
.why h2{position:absolute;left:208px;top:60px;font-size:31px;line-height:37px;font-weight:600}
.why p{position:absolute;left:208px;width:420px;font-size:14.5px;line-height:23px}
.why .btn{position:absolute;left:209px;top:359px}
.why-photo{position:absolute;left:735px;top:27px;width:560px;height:363px;border-radius:50%;background:radial-gradient(ellipse at 40% 40%,#e8d2bb 0%,#b39378 45%,#6c6472 100%)}

/* clients */
.clients{position:absolute;top:2577px;left:0;width:1200px;height:447px;background:var(--navy)}
.strip-wrap .feature-bar{position:absolute;top:2515px;left:208px;width:782px;height:123px;background:var(--white);box-shadow:var(--card-shadow)}
.clients h2{position:absolute;top:110px;width:100%;text-align:center;font-size:25px;font-weight:500;color:var(--white)}
.quote-card{position:absolute;top:170px;width:250px;height:209px;border:1px solid rgba(120,160,220,.35);border-radius:6px;background:#0c2f63;padding:20px 22px;color:var(--white)}
.quote-mark{font-size:22px;color:#5b8fd8;line-height:14px;height:20px}
.quote-card blockquote{font-size:10px;line-height:19px;height:100px}
.author{display:flex;gap:12px;align-items:center}
.avatar{width:42px;height:42px;border-radius:50%;background:linear-gradient(135deg,#7c8797,#c1c7cf)}
.author b{font-weight:400;font-size:10px;display:block}
.author span{font-size:10px;color:#4f80c8}

/* insights */
.insights{position:absolute;top:3024px;left:0;width:1200px;height:408px}
.insights .eyebrow{position:absolute;left:208px;top:69px}
.insights h2{position:absolute;left:208px;top:98px;font-size:31px;line-height:36px;font-weight:600}
.insights p{position:absolute;left:208px;top:192px;width:340px;font-size:14.5px;line-height:23px}
.insights .view-all{position:absolute;left:209px;top:277px;font-size:14px;color:var(--blue);letter-spacing:.3px}
.post{position:absolute;top:70px;width:203px;height:274px;background:var(--white);box-shadow:var(--card-shadow);border-radius:4px;overflow:hidden}
.post-photo{height:109px}
.post-body{padding:20px 20px 0}
.post time{font-size:9.5px;color:var(--muted)}
.post h3{font-size:15px;font-weight:400;line-height:19px;color:var(--blue);margin:10px 0 16px;height:57px}

/* footer */
.site-footer{position:absolute;top:3432px;left:0;width:1200px;height:318px;background:var(--navy-deep);color:var(--white)}
.footer-brand{position:absolute;left:210px;top:52px;display:flex;gap:10px;align-items:center}
.footer-brand .brand-mark{background:var(--white)}
.footer-brand .brand-name{color:var(--white);font-size:18px}
.footer-about{position:absolute;left:210px;top:112px;width:200px;font-size:9.8px;line-height:18.5px}
.footer-col{position:absolute;top:56px}
.footer-col h4{font-size:14px;font-weight:500;color:#2b6fd0;margin-bottom:16px;letter-spacing:.3px}
.footer-col ul{list-style:none;font-size:9.8px;line-height:22.5px;padding-left:3px}
.divider{position:absolute;top:52px;width:1px;height:180px;background:rgba(120,160,220,.35)}
.copyright{position:absolute;left:210px;top:270px;font-size:9.5px}
</style>
</head>
<body>

<header class="site-header">
  <a class="brand" href="#"><span class="brand-mark"></span><span class="brand-name">TARNWELL<br>AVIATION GROUP</span></a>
  <nav class="main-nav">
    <a href="#">ABOUT</a><a href="#">AIRCRAFT MANAGEMENT</a><a href="#">AIRCRAFT ACQUISITION</a><a href="#">CHARTER</a><a href="#">PILOT SERVICES</a><a href="#">TRIP SUPPORT</a><a href="#">CONTACT</a>
  </nav>
  <a class="nav-cta" href="#">REQUEST QUOTE</a>
</header>

<section class="hero">
  <div class="hero-photo" role="img" aria-label="Business jet on a runway at sunset with a jet climbing overhead"></div>
  <div class="hero-shade"></div>
  <p class="eyebrow">GLOBAL AVIATION SOLUTIONS</p>
  <h1>Precision Aviation.<br>Unified Excellence.</h1>
  <p class="hero-lede">A global aviation group delivering aircraft management, charter, training, and operational support—under one trusted name.</p>
  <div class="hero-actions">
    <a class="btn btn-primary" href="#" style="width:192px">EXPLORE SERVICES <svg width="12" height="10"><path d="M0 5h10M6 1l4 4-4 4" stroke="#fff" fill="none" stroke-width="1.4"/></svg></a>
    <a class="btn btn-outline" href="#" style="width:192px">CONTACT OUR TEAM <svg width="12" height="10"><path d="M0 5h10M6 1l4 4-4 4" stroke="#fff" fill="none" stroke-width="1.4"/></svg></a>
  </div>
  <p class="trust"><svg width="16" height="18"><path d="M8 1l6 3v5c0 4-3 6.5-6 8-3-1.5-6-4-6-8V4z" stroke="#3f7fd8" fill="none" stroke-width="1.2"/><path d="M5 9l2 2 4-4" stroke="#3f7fd8" fill="none" stroke-width="1.2"/></svg>Trusted by aviation professionals <span>worldwide</span></p>
  <div class="feature-bar">
    <div class="feature"><svg width="30" height="30"><circle cx="15" cy="15" r="13" stroke="#3f7fd8" fill="none" stroke-width="2"/><path d="M2 15h26M15 2c-6 7-6 19 0 26M15 2c6 7 6 19 0 26" stroke="#3f7fd8" fill="none" stroke-width="2"/></svg><div><h3>GLOBAL REACH</h3><p>Worldwide network and local expertise</p></div></div>
    <div class="feature"><svg width="30" height="30"><path d="M15 2l11 4v9c0 7-5 11-11 13-6-2-11-6-11-13V6z" stroke="#3f7fd8" fill="none" stroke-width="2"/><path d="M10 15l4 4 7-7" stroke="#3f7fd8" fill="none" stroke-width="2"/></svg><div><h3>SAFETY FIRST</h3><p>Uncompromising standards in every operation</p></div></div>
    <div class="feature"><svg width="30" height="30"><circle cx="15" cy="10" r="6" stroke="#3f7fd8" fill="none" stroke-width="2"/><path d="M4 28c0-7 5-10 11-10s11 3 11 10" stroke="#3f7fd8" fill="none" stroke-width="2"/></svg><div><h3>EXPERT TEAM</h3><p>Experienced professionals dedicated to you</p></div></div>
    <div class="feature"><svg width="30" height="30"><path d="M3 15h24M15 4l4 11-4 11M7 11l2 4-2 4" stroke="#3f7fd8" fill="none" stroke-width="2"/></svg><div><h3>TAILORED SOLUTIONS</h3><p>Custom aviation services built around your needs</p></div></div>
  </div>
</section>

<section class="about">
  <p class="eyebrow center">ABOUT TARNWELL</p>
  <h2 class="center">One Group. Multiple Expert Solutions.</h2>
  <p class="lead">Tarnwell Aviation Group is an umbrella organization bringing together specialized aviation companies under one unified standard of excellence.</p>
  <div class="pill-row"><span class="pill">OUR FAMILY OF COMPANIES</span></div>

  <a class="carousel-btn" href="#" style="left:153px;top:406px" aria-label="Previous"><svg width="8" height="10"><path d="M6 1L2 5l4 4" stroke="#333" fill="none" stroke-width="1.3"/></svg></a>
  <a class="carousel-btn" href="#" style="left:1018px;top:406px" aria-label="Next"><svg width="8" height="10"><path d="M2 1l4 4-4 4" stroke="#333" fill="none" stroke-width="1.3"/></svg></a>

  <article class="company-card" style="left:208px">
    <div class="company-head"><span class="icon-ring"><svg width="26" height="26"><path d="M3 13h20M13 3l5 10-5 10M6 9l2 4-2 4" stroke="#0a52a8" fill="none" stroke-width="2.2"/></svg></span><div><div class="company-name">TARNWELL</div><div class="company-sub">Aircraft Management</div></div></div>
    <p>Comprehensive aircraft management solutions designed to maximize safety, efficiency.</p>
    <a class="arrow-link" href="#">LEARN MORE <svg width="10" height="8"><path d="M0 4h8M5 1l3 3-3 3" stroke="#0a52a8" fill="none" stroke-width="1.3"/></svg></a>
  </article>
  <article class="company-card" style="left:481px">
    <div class="company-head"><span class="icon-ring"><svg width="28" height="22"><path d="M2 8l6-4 6 4 6-4 6 4v8l-6 4-6-4-6 4-6-4z" stroke="#0a52a8" fill="none" stroke-width="1.8"/></svg></span><div><div class="company-name">TARNWELL</div><div class="company-sub">Aircraft Acquisition</div></div></div>
    <p>Expert guidance for aircraft purchasing, sales, and investment decisions tailored to your goals.</p>
    <a class="arrow-link" href="#">LEARN MORE <svg width="10" height="8"><path d="M0 4h8M5 1l3 3-3 3" stroke="#0a52a8" fill="none" stroke-width="1.3"/></svg></a>
  </article>
  <article class="company-card" style="left:753px">
    <div class="company-head"><span class="icon-ring"><svg width="26" height="26"><circle cx="13" cy="9" r="5" stroke="#0a52a8" fill="none" stroke-width="2"/><path d="M3 25c0-6 4-9 10-9s10 3 10 9" stroke="#0a52a8" fill="none" stroke-width="2"/></svg></span><div><div class="company-name">TARNWELL</div><div class="company-sub">Pilot Services</div></div></div>
    <p>Professional pilot staffing, training, and operational support to meet your specific requirements.</p>
    <a class="arrow-link" href="#">LEARN MORE <svg width="10" height="8"><path d="M0 4h8M5 1l3 3-3 3" stroke="#0a52a8" fill="none" stroke-width="1.3"/></svg></a>
  </article>
</section>

<section class="services">
  <div class="services-band"></div>
  <p class="eyebrow center">OUR SERVICES</p>
  <h2 class="center">End-to-End Aviation Solutions</h2>
  <p class="lead">Tarnwell Aviation Group delivers a full spectrum of aviation services designed to simplify operations, enhance safety, and elevate every aspect of your aviation experience.</p>

  <article class="service-card" style="left:28px">
    <div class="service-photo" role="img" aria-label="Private jet parked on the apron under a dusk sky" style="background:linear-gradient(180deg,#4f6685,#a7a3a0 70%,#6d6a68)"></div>
    <span class="service-icon"><svg width="26" height="26"><path d="M3 13h20M13 4l4 9-4 9M6 10l2 3-2 3" stroke="#0a52a8" fill="none" stroke-width="1.6"/></svg></span>
    <div class="service-body"><h3>Aircraft<br>Management</h3>
      <ul class="checklist"><li>Operational Oversight</li><li>Maintenance Management</li><li>Cost Optimization</li><li>Regulatory Compliance</li></ul>
      <a class="arrow-link" href="#">LEARN MORE <svg width="10" height="8"><path d="M0 4h8M5 1l3 3-3 3" stroke="#0a52a8" fill="none" stroke-width="1.3"/></svg></a></div>
  </article>
  <article class="service-card" style="left:260px">
    <div class="service-photo" role="img" aria-label="Warm-lit private jet cabin with leather seats" style="background:linear-gradient(180deg,#3a2418,#8a5a38 55%,#c89a6e)"></div>
    <span class="service-icon"><svg width="26" height="26"><path d="M9 3v12h9l2 8M9 15l-2 8M12 3h3" stroke="#0a52a8" fill="none" stroke-width="1.6"/></svg></span>
    <div class="service-body"><h3>Charter</h3>
      <ul class="checklist"><li>Worldwide Charter Access</li><li>Business &amp; Leisure Travel</li><li>VIP Experience</li><li>Empty Leg Opportunities</li></ul>
      <a class="arrow-link" href="#">LEARN MORE <svg width="10" height="8"><path d="M0 4h8M5 1l3 3-3 3" stroke="#0a52a8" fill="none" stroke-width="1.3"/></svg></a></div>
  </article>
  <article class="service-card" style="left:492px">
    <div class="service-photo" role="img" aria-label="Close view of a jet engine on a wing" style="background:linear-gradient(180deg,#9fb3c9,#d7dde4 60%,#5d6670)"></div>
    <span class="service-icon"><svg width="28" height="22"><path d="M2 8l6-4 6 4 6-4 6 4v8l-6 4-6-4-6 4-6-4z" stroke="#0a52a8" fill="none" stroke-width="1.6"/></svg></span>
    <div class="service-body"><h3>Aircraft<br>Acquisition</h3>
      <ul class="checklist"><li>Market Analysis</li><li>Aircraft Sourcing</li><li>Negotiation Support</li><li>Transaction Management</li></ul>
      <a class="arrow-link" href="#">LEARN MORE <svg width="10" height="8"><path d="M0 4h8M5 1l3 3-3 3" stroke="#0a52a8" fill="none" stroke-width="1.3"/></svg></a></div>
  </article>
  <article class="service-card" style="left:724px">
    <div class="service-photo" role="img" aria-label="Pilots at the controls in a cockpit" style="background:linear-gradient(180deg,#c9d3dc,#6f7780 55%,#2c3038)"></div>
    <span class="service-icon"><svg width="26" height="26"><circle cx="13" cy="9" r="5" stroke="#0a52a8" fill="none" stroke-width="1.6"/><path d="M3 25c0-6 4-9 10-9s10 3 10 9" stroke="#0a52a8" fill="none" stroke-width="1.6"/></svg></span>
    <div class="service-body"><h3>Pilot<br>Services</h3>
      <ul class="checklist"><li>Pilot Staffing</li><li>Training &amp; Development</li><li>Crew Management</li><li>Compliance Support</li></ul>
      <a class="arrow-link" href="#">LEARN MORE <svg width="10" height="8"><path d="M0 4h8M5 1l3 3-3 3" stroke="#0a52a8" fill="none" stroke-width="1.3"/></svg></a></div>
  </article>
  <article class="service-card" style="left:961px">
    <div class="service-photo" role="img" aria-label="Night view of the earth with city lights" style="background:linear-gradient(180deg,#071a3d,#1b3f7a 60%,#0b2250)"></div>
    <span class="service-icon"><svg width="26" height="26"><circle cx="13" cy="13" r="11" stroke="#0a52a8" fill="none" stroke-width="1.6"/><path d="M2 13h22M13 2c-5 6-5 16 0 22M13 2c5 6 5 16 0 22" stroke="#0a52a8" fill="none" stroke-width="1.6"/></svg></span>
    <div class="service-body"><h3>Trip<br>Support</h3>
      <ul class="checklist"><li>Flight Planning</li><li>Permits &amp; Clearances</li><li>Ground Handling</li><li>24/7 Operations Center</li></ul>
      <a class="arrow-link" href="#">LEARN MORE <svg width="10" height="8"><path d="M0 4h8M5 1l3 3-3 3" stroke="#0a52a8" fill="none" stroke-width="1.3"/></svg></a></div>
  </article>
</section>

<section class="why">
  <p class="eyebrow">WHY CHOOSE TARNWELL AVIATION GROUP</p>
  <h2>Built on Trust. Focused on<br>Excellence.</h2>
  <p style="top:153px">We deliver exceptional aviation services through uncompromising safety standards, industry expertise, and a commitment to precision in every operation.</p>
  <p style="top:243px">Our integrated approach ensures seamless coordination across every service, delivering consistent quality, operational efficiency, and complete confidence for every client.</p>
  <a class="btn btn-primary" href="#" style="width:193px">EXPLORE SERVICES <svg width="12" height="10"><path d="M0 5h10M6 1l4 4-4 4" stroke="#fff" fill="none" stroke-width="1.4"/></svg></a>
  <div class="why-photo" role="img" aria-label="Business jet flying above sunlit clouds"></div>
</section>

<section class="clients">
  <h2>What Our Clients Say</h2>
  <a class="carousel-btn" href="#" style="left:153px;top:259px;border-color:#8aa4c8" aria-label="Previous"><svg width="8" height="10"><path d="M6 1L2 5l4 4" stroke="#fff" fill="none" stroke-width="1.3"/></svg></a>
  <a class="carousel-btn" href="#" style="left:1018px;top:259px;border-color:#8aa4c8" aria-label="Next"><svg width="8" height="10"><path d="M2 1l4 4-4 4" stroke="#fff" fill="none" stroke-width="1.3"/></svg></a>
  <article class="quote-card" style="left:208px">
    <div class="quote-mark">“</div>
    <blockquote>“Tarnwell Aviation Group delivers a level of professionalism and operational precision that sets them apart in the aviation industry.”</blockquote>
    <div class="author"><span class="avatar"></span><div><b>— Daniel R.</b><span>Global Financial Services Firm</span></div></div>
  </article>
  <article class="quote-card" style="left:475px">
    <div class="quote-mark">“</div>
    <blockquote>“Their team consistently ensures every trip is seamless, safe, and tailored to our exact requirements.”</blockquote>
    <div class="author"><span class="avatar"></span><div><b>— Laura K.</b><span>Private Aircraft Owner</span></div></div>
  </article>
  <article class="quote-card" style="left:741px">
    <div class="quote-mark">“</div>
    <blockquote>“From aircraft management to trip support, their reliability and expertise are unmatched.”</blockquote>
    <div class="author"><span class="avatar"></span><div><b>— Owen P.</b><span>Director of Aviation</span></div></div>
  </article>
</section>

<div class="strip-wrap">
  <div class="feature-bar">
    <div class="feature"><svg width="30" height="30"><circle cx="15" cy="15" r="13" stroke="#0a52a8" fill="none" stroke-width="2"/><path d="M2 15h26M15 2c-6 7-6 19 0 26M15 2c6 7 6 19 0 26" stroke="#0a52a8" fill="none" stroke-width="2"/></svg><div><h3>GLOBAL REACH</h3><p>Worldwide network and local expertise</p></div></div>
    <div class="feature"><svg width="30" height="30"><path d="M15 2l11 4v9c0 7-5 11-11 13-6-2-11-6-11-13V6z" stroke="#0a52a8" fill="none" stroke-width="2"/><path d="M10 15l4 4 7-7" stroke="#0a52a8" fill="none" stroke-width="2"/></svg><div><h3>SAFETY FIRST</h3><p>Uncompromising standards in every operation</p></div></div>
    <div class="feature"><svg width="30" height="30"><circle cx="15" cy="10" r="6" stroke="#0a52a8" fill="none" stroke-width="2"/><path d="M4 28c0-7 5-10 11-10s11 3 11 10" stroke="#0a52a8" fill="none" stroke-width="2"/></svg><div><h3>EXPERT TEAM</h3><p>Experienced professionals dedicated to you</p></div></div>
    <div class="feature"><svg width="30" height="30"><path d="M3 15h24M15 4l4 11-4 11M7 11l2 4-2 4" stroke="#0a52a8" fill="none" stroke-width="2"/></svg><div><h3>TAILORED SOLUTIONS</h3><p>Custom aviation services built around your needs</p></div></div>
  </div>
</div>

<section class="insights">
  <p class="eyebrow">INSIGHTS &amp; NEWS</p>
  <h2>Aviation Insights<br>That Keep You Ahead</h2>
  <p>Stay informed with expert perspectives, industry trends, and operational insights from the Tarnwell Aviation Group team.</p>
  <a class="view-all" href="#">VIEW ALL ARTICLES &nbsp;→</a>
  <article class="post" style="left:568px">
    <div class="post-photo" role="img" aria-label="Jet in flight over clouds" style="background:linear-gradient(180deg,#8b96a4,#d9d3c9 60%,#6a7078)"></div>
    <div class="post-body"><time>May 20, 2026</time><h3>Best Practices for Aircraft Management in 2025</h3><a class="arrow-link" href="#">READ ARTICLE →</a></div>
  </article>
  <article class="post" style="left:786px">
    <div class="post-photo" role="img" aria-label="Business jet silhouetted against an orange sunset" style="background:linear-gradient(180deg,#d77a2c,#f3b04a 55%,#3b2a22)"></div>
    <div class="post-body"><time>May 15, 2026</time><h3>The Future of Business Aviation: Trends to Watch</h3><a class="arrow-link" href="#">READ ARTICLE →</a></div>
  </article>
</section>

<footer class="site-footer">
  <div class="footer-brand"><span class="brand-mark"></span><span class="brand-name">TARNWELL<br>AVIATION GROUP</span></div>
  <p class="footer-about">Tarnwell Aviation Group is an umbrella organization of specialized aviation companies delivering expert solutions with a shared commitment to safety, precision, and performance.</p>
  <span class="divider" style="left:437px"></span>
  <span class="divider" style="left:646px"></span>
  <span class="divider" style="left:850px"></span>
  <div class="footer-col" style="left:475px"><h4>OUR COMPANIES</h4><ul><li>Aircraft Management</li><li>Charter</li><li>Aircraft Acquisition</li><li>Pilot Services</li><li>Trip Support</li><li>Aviation Academy</li></ul></div>
  <div class="footer-col" style="left:668px"><h4>OUR SERVICES</h4><ul><li>Aircraft Management</li><li>Charter Services</li><li>Acquisition Solutions</li><li>Pilot Staffing &amp; Training</li><li>Trip Support</li><li>Global Operations</li></ul></div>
  <div class="footer-col" style="left:874px"><h4>COMPANY</h4><ul><li>About Us</li><li>Leadership Team</li><li>Careers</li><li>Insights &amp; News</li><li>Contact Us</li></ul></div>
  <p class="copyright">© 2024 Tarnwell Aviation Group. All rights reserved.</p>
</footer>

</body>
</html>
```